Construction Company Needs Letterhead Design

We recently had a new logo designed and would like to have our letterhead updated to a trendier design. We are a concrete construction company based out of Iowa, but do work for Agricultural businesses across the Midwest.

Industry/Entity Type

Construction

Colors
ec1f27
000000
ffffff

Requirements
Must have
• Must stay within our current color scheme of red/black/white. Must have have our address, phone number, e-mail address, etc. printed on the letterhead as well.

```html
<!DOCTYPE html>
<html lang="en">
<head>
<meta charset="utf-8">
<title>Harlow Letterhead</title>
<link rel="stylesheet" href="https://fonts.googleapis.com/css2?family=PT+Sans:wght@400;700&display=swap">
<style>
  :root {
    --red: #ec1f27;
    --black: #161616;
    --white: #ffffff;
    --ink: #111111;
    --rule: #8a8a8a;
    --backdrop: #ffffff;
  }
  * { margin: 0; padding: 0; box-sizing: border-box; }
  html, body { width: 1200px; height: 1200px; overflow: hidden; background: var(--backdrop); }
  body { font-family: "PT Sans", sans-serif; color: var(--ink); position: relative; }

  .letterhead {
    position: absolute; left: 218px; top: 90px;
    width: 764px; height: 989px;
    background: var(--white);
    box-shadow: 0 0 4px rgba(0,0,0,0.12);
    overflow: hidden;
  }

  .header-band {
    position: absolute; left: 0; top: 0; width: 100%; height: 64px;
    background: var(--red);
  }
  .header-rule {
    position: absolute; left: 0; top: 72px; width: 100%; height: 6px;
    background: var(--black);
  }

  .brand {
    position: absolute; right: 98px; top: 102px;
    display: flex; align-items: center; gap: 10px;
  }
  .brand__mark { width: 36px; height: 36px; background: var(--red); }
  .brand__name {
    font-weight: 700; font-size: 40px; line-height: 1;
    color: var(--black); letter-spacing: 0.5px; text-transform: uppercase;
  }
  .brand__rule {
    position: absolute; right: 98px; top: 160px; width: 196px; height: 1px; background: var(--rule);
  }

  .contact {
    position: absolute; right: 98px; top: 181px;
    text-align: right; font-size: 12.5px; line-height: 16.8px; letter-spacing: 0.8px;
    list-style: none;
  }

  .letter { position: absolute; left: 96px; top: 311px; width: 570px; }
  .letter__title {
    font-size: 16px; font-weight: 700; letter-spacing: 1px; margin-bottom: 40px;
  }
  .letter__body p {
    font-size: 12.6px; line-height: 16.5px; letter-spacing: 0.75px;
    text-align: justify; hyphens: auto; margin-bottom: 16px;
  }
  .letter__body p + p { text-indent: 44px; }

  .signature {
    position: absolute; right: 98px; top: 862px; width: 201px;
    border-top: 1px solid var(--rule);
    text-align: right; font-size: 12px; letter-spacing: 0.8px; padding-top: 6px;
  }

  .footer-rule {
    position: absolute; left: 0; bottom: 50px; width: 100%; height: 4px;
    background: var(--red);
  }
  .footer-band {
    position: absolute; left: 0; bottom: 0; width: 100%; height: 40px;
    background: var(--black);
  }
</style>
</head>
<body>
  <article class="letterhead">
    <div class="header-band"></div>
    <div class="header-rule"></div>

    <div class="brand">
      <span class="brand__mark"></span>
      <span class="brand__name">Harlow</span>
    </div>
    <div class="brand__rule"></div>

    <ul class="contact">
      <li>0123 Zip abc City USA</li>
      <li>+00 1234 56 789</li>
      <li>mail@company.com</li>
      <li>www.company.com</li>
    </ul>

    <section class="letter">
      <h1 class="letter__title">Section 1.10.32 of "de Finibus Bonorum et Malorum"</h1>
      <div class="letter__body">
        <p>"Sed ut perspiciatis unde omnis iste natus error sit voluptatem accusantium doloremque laudantium, totam rem aperiam, eaque ipsa quae ab illo inventore veritatis et quasi architecto beatae vitae dicta sunt explicabo. Nemo enim ipsam voluptatem quia voluptas sit aspernatur aut odit aut fugit, sed quia consequuntur magni dolores eos qui ratione voluptatem sequi nesciunt. Neque porro quisquam est, qui dolorem ipsum quia dolor sit amet, consectetur, adipisci velit, sed quia non numquam eius modi tempora incidunt ut labore et dolore magnam aliquam quaerat voluptatem. Ut enim ad minima veniam, quis nostrum exercitationem ullam corporis suscipit laboriosam, nisi ut aliquid ex ea commodi consequatur? Quis autem vel eum iure reprehenderit qui in ea voluptate velit esse quam nihil molestiae consequatur, vel illum qui dolorem eumfugiat voluptas nulla pariatur?"</p>
        <p>"At vero eos et accusamus et iusto odio dignissimos ducimus qui blanditiis praesentium voluptatum deleniti atque corrupti quos dolores et quas molestias excepturi sint occaecati cupiditate non provident, similique sunt in culpa qui officia deserunt mollitia animi, id est laborum et dolorum fuga. Et harum quidem rerum facilis est et expedita distinctio. Nam libero tempore, cum soluta nobis est eligendi optio cumque nihil impedit quo minus id quod maxime placeat facere possimus, omnis voluptas assumenda est, omnis dolor repellendus. Temporibus autem quibusdam et aut officiis debitis aut rerum necessitatibus saepe eveniet ut et voluptates repudiandae sint et molestiae non recusandae. Itaque earum rerum hic tenetur a sapiente delectus, ut aut reiciendis voluptatibus maiores alias consequatur aut perferendis doloribus asperiores repellat."</p>
      </div>
    </section>

    <div class="signature">signature</div>

    <div class="footer-rule"></div>
    <div class="footer-band"></div>
  </article>
</body>
</html>
```